business card for dental office

We need a business card design for an existing company follwing information we need on the card:
Teodor L Vanwick, DDS
4263 Harlowe Court
Larkmoor, MD 21907
Ph: 703-555-0142 Fax:703-555-0187
www.grinvalemont.example info@grinvalemont.example
second side
Appointment
For
Date: day:
Time
if you are unable to keep your appointment, please contact us 24 hours in advance.
Note: Logo is attached to use with the card
Thanks
Industry/Entity Type
Dental Clinic
Contact Information for Business Card
Teodor L Vanwick, DDS
4263 Harlowe Court
Larkmoor, MD 21907
second side
Appointment
For
Date: day:
Time
Thanks

```html
<!DOCTYPE html>
<html lang="en">
<head>
<meta charset="utf-8">
<title>Grinvalemont Dental Associates – Business Card</title>
<link rel="stylesheet" href="https://fonts.googleapis.com/css2?family=Source+Sans+3:wght@400;600;700&display=swap">
<style>
  :root {
    --stage: #000000;
    --card: #ffffff;
    --navy: #1c3e7c;
    --ink: #1a1a1a;
    --sky: #2aa3dc;
  }
  * { margin: 0; padding: 0; box-sizing: border-box; }
  html, body { width: 1200px; height: 900px; overflow: hidden; background: var(--stage); }
  body { position: relative; font-family: "Source Sans 3", sans-serif; color: var(--ink); }

  .card { position: absolute; background: var(--card); top: 275px; height: 294px; width: 477px; }
  .card--front { left: 116px; border-radius: 0 58px 0 62px; }
  .card--back { left: 622px; top: 276px; height: 293px; border-radius: 58px 0 58px 0; }

  .dentist-name {
    position: absolute; right: 26px; top: 29px;
    font-size: 17.5px; font-weight: 600; color: var(--navy);
  }

  .brand { position: absolute; display: flex; align-items: center; gap: 8px; color: var(--navy); font-weight: 600; }
  .brand__dot { width: 12px; height: 12px; border-radius: 50%; background: var(--sky); flex: none; }
  .card--front .brand { left: 30px; top: 88px; font-size: 19px; line-height: 1.1; }
  .brand__name small { display: block; font-size: 13px; letter-spacing: 3px; }
  .card--back .brand { left: 0; right: 0; top: 34px; justify-content: center; font-size: 20px; }

  .address {
    position: absolute; right: 27px; top: 140px;
    text-align: right; font-size: 14px; line-height: 20px; font-style: normal;
  }
  .contacts { position: absolute; right: 25px; top: 188px; list-style: none; font-size: 14px; }
  .contacts li { display: flex; justify-content: flex-end; align-items: center; gap: 8px; height: 20px; }
  .contacts svg { width: 10px; height: 10px; fill: var(--navy); flex: none; }

  .appointment-title {
    position: absolute; left: 0; right: 0; top: 84px;
    text-align: center; font-size: 21px; font-weight: 700; color: var(--navy);
  }
  .form { position: absolute; left: 70px; right: 70px; top: 136px; font-size: 13px; }
  .form__row { display: flex; align-items: baseline; height: 33px; }
  .form__label { flex: none; margin-right: 6px; }
  .form__fill { flex: 1; border-bottom: 1.5px dotted var(--ink); margin-right: 4px; }
  .form__unit { flex: none; margin-right: 4px; }
  .notice {
    position: absolute; left: 0; right: 0; top: 244px;
    text-align: center; font-size: 14.5px; font-weight: 600; color: var(--navy);
  }
</style>
</head>
<body>
  <section class="card card--front">
    <h1 class="dentist-name">Teodor L Vanwick, DDS</h1>
    <div class="brand">
      <span class="brand__dot"></span>
      <span class="brand__name">Grinvalemont Dental<small>associates</small></span>
    </div>
    <address class="address">4263 Harlowe Court<br>Larkmoor, MD 21907</address>
    <ul class="contacts">
      <li>555-555-0142
        <svg viewBox="0 0 10 10"><path d="M2 0.5 L3.6 2.6 L2.8 3.6 C3.5 5 5 6.5 6.4 7.2 L7.4 6.4 L9.5 8 L8.4 9.5 C4.5 9 1 5.5 0.5 1.6 Z"/></svg>
      </li>
      <li>555-555-0187
        <svg viewBox="0 0 10 10"><rect x="0.5" y="3" width="9" height="6.5" rx="1"/><rect x="2.5" y="0.5" width="5" height="3" fill="none" stroke="#1c3e7c"/></svg>
      </li>
      <li>info@grinvalemont.example
        <svg viewBox="0 0 10 10"><rect x="0.5" y="1.5" width="9" height="7"/><path d="M0.5 1.5 L5 5.5 L9.5 1.5" fill="none" stroke="#fff"/></svg>
      </li>
      <li>www.grinvalemont.example
        <svg viewBox="0 0 10 10"><path d="M4 6 L6 4 M3 5 L1.5 6.5 a1.6 1.6 0 0 0 2 2 L5 7 M7 5 L8.5 3.5 a1.6 1.6 0 0 0 -2 -2 L5 3" fill="none" stroke="#1c3e7c" stroke-width="1.2"/></svg>
      </li>
    </ul>
  </section>

  <section class="card card--back">
    <div class="brand">
      <span class="brand__dot"></span>
      <span>Grinvalemont Dental Associates</span>
    </div>
    <h2 class="appointment-title">Your Next Appointment is</h2>
    <div class="form">
      <div class="form__row"><span class="form__label">Name :</span><span class="form__fill"></span></div>
      <div class="form__row"><span class="form__label">Date :</span><span class="form__fill"></span></div>
      <div class="form__row"><span class="form__label">Time:</span><span class="form__fill"></span><span class="form__unit">AM</span><span class="form__fill"></span><span class="form__unit">PM</span></div>
    </div>
    <p class="notice">If unable to keep appointment, kindly give 24hrs notice.</p>
  </section>
</body>
</html>
```